Book on a defense of Christianity needs a cover design.

I need a cover for a book providing a fair and balanced factually supported logical defense of three sources related to Christian beliefs: Old Testament, New Testament, and Book of Mormon. It is written in easy to follow language in a father-to-son question and answer format. There are extensive footnotes that allow the reader to go to the source and research all things stated in the book. Both the positive evidence and the negative evidence is presented in respectful language. The final point is a proof of the validity of Christian basic beliefs. The title of the book is: Listen Well, Young One: When Doubt Comes Knocking. Letters from a father to his son regarding an evidence based logical approach to combat the secular attacks on Christianity.
Target Market(s)
General public
Industry/Entity Type
Defense
Requirements
Nice to have
- Color. Attention grabbing design. Can be abstract.

```html
<!DOCTYPE html>
<html lang="en">
<head>
<meta charset="utf-8">
<title>Listen Well, Young One — Cover</title>
<link rel="stylesheet" href="https://fonts.googleapis.com/css2?family=Libre+Baskerville:wght@700&family=Lato:wght@400&display=swap">
<style>
  :root {
    --page-bg: #e9e7e3;
    --sky-top: #6f6a63;
    --sky-glow: #d9b08f;
    --sky-warm: #c49274;
    --tree-line: #3d4a2c;
    --water-top: #6b6a4a;
    --water-deep: #4a4632;
    --dock: #6a4a36;
    --dock-dark: #3e2a1f;
    --title: #ffffff;
    --author: #e6c35c;
  }
  html, body {
    margin: 0;
    width: 1200px;
    height: 800px;
    overflow: hidden;
    background: var(--page-bg);
  }
  .canvas {
    position: relative;
    width: 1200px;
    height: 800px;
  }
  .cover {
    position: absolute;
    left: 360px;
    top: 40px;
    width: 480px;
    height: 720px;
    overflow: hidden;
    box-shadow: 0 10px 30px rgba(0,0,0,0.18);
  }
  .cover-scene {
    position: absolute;
    inset: 0;
    background: linear-gradient(180deg,
      var(--sky-top) 0%,
      var(--sky-warm) 14%,
      var(--sky-glow) 24%,
      var(--tree-line) 34%,
      var(--tree-line) 40%,
      var(--water-top) 46%,
      var(--water-deep) 64%,
      var(--dock) 78%,
      var(--dock-dark) 100%);
  }
  .cover-title {
    position: absolute;
    top: 78px;
    left: 0;
    right: 0;
    margin: 0;
    text-align: center;
    font-family: "Libre Baskerville", Georgia, serif;
    font-weight: 700;
    font-size: 44px;
    line-height: 1.06;
    letter-spacing: -0.5px;
    color: var(--title);
    text-transform: uppercase;
    text-shadow: 0 2px 6px rgba(0,0,0,0.35);
  }
  .cover-subtitle {
    position: absolute;
    top: 196px;
    left: 0;
    right: 0;
    margin: 0;
    text-align: center;
    font-family: "Lato", Arial, sans-serif;
    font-size: 15px;
    letter-spacing: 1px;
    color: var(--title);
    text-transform: uppercase;
  }
  .cover-author {
    position: absolute;
    bottom: 26px;
    left: 0;
    right: 0;
    margin: 0;
    text-align: center;
    font-family: "Libre Baskerville", Georgia, serif;
    font-weight: 700;
    font-size: 17px;
    letter-spacing: 1px;
    color: var(--author);
    text-transform: uppercase;
  }
</style>
</head>
<body>
  <main class="canvas">
    <section class="cover">
      <div class="cover-scene" role="img" aria-label="Photograph of a father and young son seen from behind, fishing from a wooden dock on a calm lake at sunset, with trees along the far shore"></div>
      <h1 class="cover-title">Listen Well,<br>Young One</h1>
      <p class="cover-subtitle">When Doubt Comes Knocking</p>
      <p class="cover-author">Daniel Okoro</p>
    </section>
  </main>
</body>
</html>
```